I need a Cool Physio Postcard / Flyer

HI!
We need a double sided, postcard sized, promotional card (not an actual postcard) to distribute to gyms and sporting clubs, promoting our physiotherapy clinic.
The main colours of our brand are navy blue & white (As seen in sample files).
I want it to be HORIZONTAL
On one side i'd like our logo / image.
The name - "Heel & Stride Recovery Australia" and the tagline - "“Australia’s trusted lower limb recovery team.”
• Fast Rehab for lower limb injury and surgery
• Mobilisation of the foot and ankle
• Hands on therapy
• National sporting team expertise
• Podiatry (Toe-nail, skin, diabetic foot care, orthotics)
• Video pressure treadmill gait analysis and correction
• Running assessment
• Nordic walking training and sessions
Also our website: www.HSRA-demo.com.au & a Pagebook icon next to www.Pagebook-demo.com/HSRA
Also see the sample image of the runner and blue colouring. I would like this included somewhere on the postcard. I'd like to see some different design options implementing the image in different ways (front or back).
On the other side of the card I want the following text:
"HSRA is Victoria’s leading specialist provider of rehabilitation for Foot & Ankle injury and surgery.
We see our patients through their rehabilitation with an unmatched level of care and expertise.
Whether you’re an elite athlete, a weekend walker or strolling to the office, we provide the highest quality treatment and support to quickly get you back to your usual functional capacity, moving pain free with confidence.
Make an appointment at one of our FOUR Victorian locations today!”
Richmond
Summit Motion Clinic
Level 1, 418 Wattle St
Richmond 3121
1300 642 913 Frankston
Suite 6, 371 Pemberton Drive
Frankston 3199
9483 2295
Brighton
Suite 4, 937 Elm Street
Brighton 3186
9371 4058
Geelong
146 Kingsley Terrace
Geelong 3220
5264 3719
Please display our four locations in a similar fashion to the white screenshot ive attached.
The images I included of my draft design are just to provide you an idea or some inspiration of what I’m after. Please feel free to use your creativity.. Good Luck!
Reason: I accidentally didn't put a design brief in for the first 6 days of the project. The designs only started arriving 4 days ago once I corrected this mistake.
I need more time to provide feedback & get exactly what I want.
Thanks in advance
Reid

```html
<!DOCTYPE html>
<html lang="en">
<head>
<meta charset="utf-8">
<title>HSRA – Locations Card</title>
<link rel="stylesheet" href="https://fonts.googleapis.com/css2?family=PT+Sans:wght@400;700&display=swap">
<style>
  :root {
    --navy: #0071b9;
    --sky: #08a0db;
    --white: #ffffff;
    --page: #ffffff;
  }
  * { margin: 0; padding: 0; box-sizing: border-box; }
  html, body {
    width: 1200px; height: 868px; overflow: hidden;
    background: var(--page);
    font-family: "PT Sans", "Myriad Pro", sans-serif;
    color: var(--white);
  }
  .card { position: relative; width: 1200px; height: 868px; }

  .intro {
    position: absolute; left: 80px; top: 55px; width: 1039px; height: 283px;
    background: var(--navy);
    padding: 25px 28px 0 39px;
    font-size: 22px; line-height: 30px;
    text-align: justify;
  }
  .intro p + p { margin-top: 30px; }

  .cta {
    position: absolute; left: 80px; top: 361px; width: 281px; height: 430px;
    background: var(--navy);
    display: flex; align-items: center; justify-content: center;
    text-align: center;
    font-weight: 700; font-size: 33px; line-height: 43.5px;
    padding: 0 16px;
  }

  .location {
    position: absolute; width: 352px; height: 203px;
    font-size: 22px; line-height: 30px;
  }
  .location--navy { background: var(--navy); }
  .location--sky { background: var(--sky); }
  .location__name { font-weight: 700; }

  .location--richmond { left: 389px; top: 361px; padding: 40px 0 0 61px; }
  .location--frankston { left: 767px; top: 361px; padding: 25px 0 0 67px; }
  .location--brighton { left: 389px; top: 589px; padding: 41px 0 0 63px; }
  .location--geelong { left: 767px; top: 589px; padding: 41px 0 0 75px; }
</style>
</head>
<body>
<main class="card">
  <section class="intro">
    <p>HSRA is Victoria’s leading specialist provider of rehabilitation for Foot &amp; Ankle injury and surgery.</p>
    <p>We see our patients through their rehabilitation with an unmatched level of care and expertise.</p>
    <p>Whether you’re an elite athlete, a weekend walker or strolling to the office, we provide the highest quality treatment and support to quickly get you back to your usual functional capacity, moving pain free with confidence.</p>
  </section>

  <h2 class="cta">Make an appointment at one of our FOUR Victorian locations today!</h2>

  <address class="location location--navy location--richmond" style="font-style:normal">
    <div class="location__name">Richmond</div>
    <div>Level 1, 418 Wattle St</div>
    <div>Richmond 3121</div>
    <div>1300 642 913</div>
  </address>

  <address class="location location--sky location--frankston" style="font-style:normal">
    <div class="location__name">Frankston</div>
    <div>Suite 6,</div>
    <div>371 Pemberton Drive</div>
    <div>Frankston 3199</div>
    <div>9483 2295</div>
  </address>

  <address class="location location--sky location--brighton" style="font-style:normal">
    <div class="location__name">Brighton</div>
    <div>Suite 4, 937 Elm Street</div>
    <div>Brighton 3186</div>
    <div>9371 4058</div>
  </address>

  <address class="location location--navy location--geelong" style="font-style:normal">
    <div class="location__name">Geelong</div>
    <div>146 Kingsley Terrace</div>
    <div>Geelong 3220</div>
    <div>5264 3719</div>
  </address>
</main>
</body>
</html>
```